B2B EDM Banner Design- Specialist Tech Company

We need a new top-of-email banner for our EDM campaigns for Brelmont Digest (www.brelmontdigest.example
). This banner will sit at the top of every email and must immediately signal the brand, look modern and professional, and be visually aligned with the tech/IT audience.
Size of the banner: Around 728x90 - it must fit at the top of an email blast.
Purpose of the Banner
Establish a strong, recognizable brand identity across all Brelmont Digest EDMs
visually consistent with existing banners created for other brands (see reference examples provided)
Communicate Brelmont Digest’s value proposition at a glance
Brand Name
Brelmont Digest
Tagline (must appear in the banner)
“11,322 whitepapers from 726 companies”
Design Requirements
Style & Tone
Modern, clean, and professional
Tech-centric look and feel
High-quality, sleek, and corporate
Eye-catching but not cluttered
Should feel premium and authoritative
Layout & Composition
Full-width banner for email header
Horizontal orientation similar to the StaffLoom and Workforce Paper Vault examples
Include space for the brand name/logo prominently on the left or centered
Integrate the tagline in a readable, secondary position
Optional: a subtle background texture or tech-related abstract pattern (circuitry, network nodes, gradient, etc.)
No busy imagery—should feel clean and trustworthy
Color Palette
Use colors consistent with Brelmont Digest branding from www.brelmontdigest.example
Blues, greys, blacks, and tech-style gradients preferred
Should feel consistent with a B2B IT audience
Typography
Clean, sans-serif fonts (professional/tech-aligned)
Brand name should be bold and prominent
Tagline should be smaller, but still readable on desktop and mobile
Imagery (if used)
Abstract tech shapes, network visuals, geometric patterns, or gradient overlays
Avoid photography of people
Keep imagery subtle so text remains legible
Call-to-Action Button (optional)
None required in this banner (unlike the HR examples)
Banner should remain a pure brand header
Deliverables
Final banner in PNG and JPG formats
2–3 design variations (if possible) for A/B testing
Dimensions optimized for EDM: ~600–700px wide (standard email width), proportionate height

```html
<!DOCTYPE html>
<html lang="en">
<head>
<meta charset="utf-8">
<title>Brelmont Digest — Email Header</title>
<link rel="stylesheet" href="https://fonts.googleapis.com/css2?family=Montserrat:wght@300;700&display=swap">
<style>
  :root {
    --side-grey: #ebebeb;
    --side-grey-light: #f3f3f3;
    --navy-deep: #06143d;
    --navy-mid: #0b2263;
    --network-blue: #1a4fc4;
    --brand-cyan: #1e9ad6;
    --text-white: #ffffff;
  }
  * { margin: 0; padding: 0; box-sizing: border-box; }
  html, body {
    width: 1200px;
    height: 240px;
    overflow: hidden;
    background: var(--side-grey);
  }
  .banner {
    position: relative;
    width: 1200px;
    height: 240px;
    background: linear-gradient(180deg, var(--side-grey-light), var(--side-grey));
    font-family: "Montserrat", sans-serif;
  }
  .brand-panel {
    position: absolute;
    left: 282px;
    top: 0;
    width: 790px;
    height: 240px;
    overflow: hidden;
    background: linear-gradient(100deg, var(--navy-deep) 0%, var(--navy-mid) 70%, #0d2a78 100%);
  }
  .network-visual {
    position: absolute;
    right: 0;
    top: 0;
    width: 520px;
    height: 240px;
    background:
      radial-gradient(ellipse 60% 70% at 80% 20%, rgba(40, 110, 230, 0.55), transparent 70%),
      radial-gradient(ellipse 45% 55% at 40% 50%, rgba(26, 79, 196, 0.35), transparent 75%),
      radial-gradient(ellipse 40% 50% at 95% 90%, rgba(40, 110, 230, 0.4), transparent 75%);
  }
  .brand-lockup {
    position: absolute;
    left: 92px;
    top: 48px;
    display: flex;
    align-items: center;
    gap: 24px;
  }
  .brand-mark {
    width: 84px;
    height: 84px;
    border-radius: 50%;
    background: var(--brand-cyan);
    flex: none;
  }
  .brand-name {
    color: var(--text-white);
    font-weight: 700;
    font-size: 42px;
    letter-spacing: 0.5px;
    text-transform: uppercase;
    line-height: 1;
    white-space: nowrap;
  }
  .tagline {
    position: absolute;
    left: 93px;
    top: 145px;
    color: var(--text-white);
    font-weight: 300;
    font-size: 16.5px;
    white-space: nowrap;
  }
</style>
</head>
<body>
  <div class="banner">
    <div class="brand-panel">
      <div class="network-visual" role="img" aria-label="Abstract glowing blue network of connected nodes and lines"></div>
      <div class="brand-lockup">
        <div class="brand-mark"></div>
        <div class="brand-name">Brelmont Digest</div>
      </div>
      <p class="tagline">11,322 whitepapers from 726 companies</p>
    </div>
  </div>
</body>
</html>
```